Small business providing disability support care requires services promotional poster

We need a digital poster to promote our services to PSAF service providers. We deliver individualised support to people living with disabilities of all ages. (Examples -Physical, intellectual, autism, hearing/vision impaired).We need the poster to highlight the services we offer - attached for convenience + group support, holiday support, camping and outdoor activities. We already have our own logo, we would like the colour theme to fit the logo aesthetic - attached. The design should communicate respect, holistic and collaborative care, fun and inclusivity.
RW Care Supports ( former name - Talvoro Vigour & Motion)

Target Market(s)

PSAF service providers (ROT, Support Coordinators, PSAF participants, Support agencies)

Industry/Entity Type

Community Services

Font styles to use
Sans Serif

Requirements
Must have
• Person centred positive imagery and language
Should not have
• Typical wheelchair or 'disabled' visuals, no puzzle pieces. Not too bright or busy - sensory overload

```html
<!DOCTYPE html>
<html lang="en">
<head>
<meta charset="utf-8">
<title>RW Care Supports – Services Poster</title>
<link href="https://fonts.googleapis.com/css2?family=Archivo+Black&family=Montserrat:wght@300;400;600;700;800&display=swap" rel="stylesheet">
<style>
  :root{
    --rust:#c4703e;
    --rust-deep:#b8643a;
    --peach:#f0b08a;
    --peach-soft:#f5c4a4;
    --icon-bg:#f3b994;
    --ink:#2e1b10;
    --white:#ffffff;
  }
  *{margin:0;padding:0;box-sizing:border-box}
  html,body{width:849px;height:1200px;overflow:hidden;background:var(--rust)}
  .poster{
    position:relative;width:849px;height:1200px;overflow:hidden;
    background:linear-gradient(180deg,var(--rust) 0%,var(--rust-deep) 100%);
    font-family:"Montserrat",sans-serif;color:var(--white);
  }
  .lower-glow{
    position:absolute;left:0;top:700px;width:849px;height:500px;
    background:linear-gradient(200deg,rgba(240,176,138,0) 35%,rgba(240,176,138,.7) 75%,var(--peach) 100%);
  }
  .headline{position:absolute;left:0;top:0;width:849px;height:360px}
  .headline text{font-family:"Archivo Black",sans-serif;fill:var(--white)}

  .brand-badge{
    position:absolute;left:520px;top:268px;width:212px;height:212px;border-radius:50%;
    background:var(--peach);border:4px solid var(--peach-soft);
    display:flex;align-items:center;justify-content:center;text-align:center;
  }
  .brand-name{font-weight:800;font-size:28px;line-height:1.08;color:var(--ink)}

  .photo{position:absolute;border-radius:50%;border:5px solid var(--peach-soft)}
  .photo-main{left:277px;top:373px;width:286px;height:286px;background:linear-gradient(160deg,#e9d7c4,#9fa9b8 60%,#7b6a63)}
  .photo-mid{left:448px;top:472px;width:198px;height:198px;background:linear-gradient(160deg,#c9a58a,#d99a72)}
  .photo-right{left:600px;top:498px;width:200px;height:200px;background:linear-gradient(160deg,#efe6dc,#b98c73 60%,#5d4a44)}

  .intro{
    position:absolute;left:48px;top:376px;z-index:2;
    font-size:17.5px;font-weight:300;line-height:20px;white-space:nowrap;
  }
  .conditions{
    position:absolute;left:48px;top:555px;z-index:2;
    font-size:21px;font-weight:700;line-height:24px;white-space:nowrap;
  }

  .service-icon{position:absolute;border-radius:50%;background:var(--icon-bg)}
  .icon-left{left:40px;width:60px;height:60px}
  .icon-right{left:384px;width:56px;height:56px}
  .service{position:absolute;color:var(--ink);font-size:9.8px;line-height:12.4px}
  .service-left{left:131px;width:262px}
  .service-right{left:453px;width:350px}
  .service-title{font-weight:700}
  .service-list{list-style:none}
  .service-list li::before{content:"• "}

  .contact{position:absolute;left:48px;top:1083px;color:var(--ink)}
  .contact-name{font-size:18px;font-weight:400;margin-bottom:5px}
  .contact-line{display:flex;align-items:center;gap:10px;font-size:18px;margin-bottom:4px}
  .contact-line svg{width:18px;height:18px;fill:var(--ink)}
</style>
</head>
<body>
<div class="poster">
  <div class="lower-glow"></div>

  <svg class="headline" viewBox="0 0 849 360" role="heading" aria-level="1" aria-label="We deliver individualised support to people living with disabilities of all ages">
    <text x="54" y="86" font-size="50" textLength="493" lengthAdjust="spacingAndGlyphs">We deliver individualised</text>
    <text x="54" y="216" font-size="180" textLength="645" lengthAdjust="spacingAndGlyphs">support</text>
    <text x="54" y="294" font-size="42" textLength="387" lengthAdjust="spacingAndGlyphs">to people living with</text>
    <text x="54" y="341" font-size="42" textLength="424" lengthAdjust="spacingAndGlyphs">disabilities of all ages</text>
  </svg>

  <div class="brand-badge"><span class="brand-name">RW<br>Care Supports</span></div>

  <div class="photo photo-main" role="img" aria-label="Support worker serving a meal to an older man at home"></div>
  <div class="photo photo-mid" role="img" aria-label="Smiling support worker wearing a lanyard"></div>
  <div class="photo photo-right" role="img" aria-label="Young man and support worker laughing together at a table"></div>

  <p class="intro">RW CARE SUPPORTS will<br>provide supports in a<br>person centered and<br>individualised manner to<br>participants of the PSAF.<br>Every participant will be<br>unique in the supports<br>they want and require.</p>
  <p class="conditions">From physical and<br>intellectual conditions<br>to those diagnosed with<br>autism and hearing/vision<br>impairment and every<br>condition in between!</p>

  <div class="service-icon icon-left" style="top:728px" role="img" aria-label="Household chores icon"></div>
  <div class="service service-left" style="top:730px"><span class="service-title">Help Around the House</span> - Various forms of day to day assistance around the house.
    <ul class="service-list"><li>Assisting with yard care and home maintenance</li><li>Cleaning, cooking and washing</li><li>Home office duties</li></ul></div>

  <div class="service-icon icon-left" style="top:804px" role="img" aria-label="Meal preparation icon"></div>
  <div class="service service-left" style="top:800px"><span class="service-title">In-Home Care</span> - Support with routines around school, work and medication.
    <ul class="service-list"><li>Supervising or assisting with meal preparation</li><li>Help with morning and evening routines</li><li>Assistance with budgeting and paying bills</li><li>Assistance with Independent Living Skills</li></ul></div>

  <div class="service-icon icon-left" style="top:889px" role="img" aria-label="Empowerment icon"></div>
  <div class="service service-left" style="top:886px"><span class="service-title">Individual Empowerment</span> - Support to build capacity to become more independent
    <ul class="service-list"><li>Assistance with effective decision making</li><li>Assisting with advocacy and discussions with Service Providers at the request of the participant</li><li>Ensuring choice and control is being upheld by participant</li><li>Supporting the participant to understand choices with informed consent</li></ul></div>

  <div class="service-icon icon-left" style="top:1004px" role="img" aria-label="Personal care icon"></div>
  <div class="service service-left" style="top:1006px"><span class="service-title">Personal Care</span> - Assistance with day to day health and hygiene care.
    <ul class="service-list"><li>Showering</li><li>Bathroom assistance</li><li>Meal assistance</li></ul></div>

  <div class="service-icon icon-right" style="top:730px" role="img" aria-label="Community outings icon"></div>
  <div class="service service-right" style="top:730px"><span class="service-title">Out and About</span> - Assistance with accessing the community.
    <ul class="service-list"><li>Support in taking a class to learn new skills</li><li>Volunteering in the community</li><li>Going to social activities</li><li>Sport and recreational activities (camping, fishing, bush walking and more)</li></ul></div>

  <div class="service-icon icon-right" style="top:806px" role="img" aria-label="Education icon"></div>
  <div class="service service-right" style="top:812px"><span class="service-title">Education and Employment</span> - Learning and developing employable skills.
    <ul class="service-list"><li>Developing skills in School, University and Work</li><li>Assistance with completing assignments</li><li>Transition from school to further learning, work experience or work</li></ul></div>

  <div class="service-icon icon-right" style="top:891px" role="img" aria-label="Travel icon"></div>
  <div class="service service-right" style="top:894px"><span class="service-title">Transport</span> - Assistance to get from A to B.
    <ul class="service-list"><li>Getting to appointments and therapy supports</li><li>Day to day activities</li><li>Transport to education or work</li><li>Travel Training to build individual capacity to independently travel</li><li>Driving Hours for participants wanting to increase their current learner permit hours</li></ul></div>

  <div class="service-icon icon-right" style="top:1006px" role="img" aria-label="Fitness icon"></div>
  <div class="service service-right" style="top:1006px"><span class="service-title">Personal Training</span> - Improving Fitness with participants. (I can not train participants with major health concerns or complex physical therapy needs unless instructed by a physiotherapist or their Health Care Professional.)
    <ul class="service-list"><li>Resistance Training</li><li>Powerlifting Training</li><li>Boxing</li><li>General sport practice</li></ul></div>

  <div class="service-icon icon-right" style="top:1110px" role="img" aria-label="Respite stay icon"></div>
  <div class="service service-right" style="top:1118px"><span class="service-title">Respite Care</span> - Support in Direct Support Worker's home.
    <ul class="service-list"><li>Provide support in your home</li><li>Overnight Stay</li><li>Support with night and morning routine</li></ul></div>

  <div class="contact">
    <p class="contact-name">RW Care Supports</p>
    <p class="contact-line"><svg viewBox="0 0 24 24" aria-hidden="true"><path d="M6.6 10.8a15.1 15.1 0 0 0 6.6 6.6l2.2-2.2a1 1 0 0 1 1-.25 11.4 11.4 0 0 0 3.6.57 1 1 0 0 1 1 1V20a1 1 0 0 1-1 1A17 17 0 0 1 3 4a1 1 0 0 1 1-1h3.5a1 1 0 0 1 1 1c0 1.25.2 2.45.57 3.57a1 1 0 0 1-.25 1z"/></svg>0491 570 162</p>
    <p class="contact-line"><svg viewBox="0 0 24 24" aria-hidden="true"><path d="M2 11 22 3l-7 19-3.5-7.5z"/></svg>hello@rwcaresupports.com.au</p>
  </div>
</div>
</body>
</html>
```